Presentation Folder Cover For Plumbing Company

We need a presentation folder cover (FRONT AND BACK) for our plumbing business.

We specialise in plumbing, hot water, electrical and pipe relining.

This will be sent to clients and the contents pages will outline all of our company details and information.

The target market for this cover is Strata / Property Managers who look after unit buildings.

Target Market(s)

Strata & Property Managers. The higher end of the property market.

Industry/Entity Type

Plumbing

Font styles to use
Sans Serif

Colors
ec1f27
0355a3
ffffff
474747
c9c9c9

Requirements
Must have
• A4 Paper Size
• Inviting to clients to open the document and read on.
Nice to have
• Sleek, Professional and Stands Out.
Should not have
• Dark Background. Needs to be fresh and bright.

```html
<!DOCTYPE html>
<html lang="en">
<head>
<meta charset="utf-8">
<title>Harlow Contracting – Presentation Folder</title>
<link rel="stylesheet" href="https://fonts.googleapis.com/css2?family=Montserrat:wght@400;500;600;800&family=Teko:wght@500&display=swap">
<style>
  :root {
    --red: #ec1f27;
    --deep-red: #b5161c;
    --blue: #0355a3;
    --white: #ffffff;
    --charcoal: #474747;
    --ink: #222326;
    --silver: #c9c9c9;
    --stage: #dcdcdc;
  }
  * { box-sizing: border-box; margin: 0; padding: 0; }
  html, body { width: 1200px; height: 809px; overflow: hidden; }
  body { font-family: "Montserrat", Arial, sans-serif; background: var(--stage); }
  .canvas {
    position: relative; width: 1200px; height: 809px;
    background: radial-gradient(ellipse at 50% 40%, #ececec 0%, var(--stage) 70%);
  }
  .folder { position: absolute; left: 91px; top: 44px; width: 1018px; height: 720px; display: flex;
    box-shadow: 0 18px 40px rgba(0,0,0,.25); }
  .panel { position: relative; width: 509px; height: 720px; overflow: hidden; }
  .panel svg.art { position: absolute; inset: 0; width: 509px; height: 720px; }
  .panel--back { background: linear-gradient(135deg, #f7f7f7 0%, #e6e6e6 60%, #f2f2f2 100%); }
  .panel--front { background: var(--white); }

  /* back panel */
  .watermark { position: absolute; left: 0; right: 0; top: 250px; text-align: center; color: rgba(0,0,0,.06); }
  .watermark__name { font-weight: 800; font-size: 44px; letter-spacing: 1px; line-height: 1.1; }
  .watermark__trades { font-weight: 500; font-size: 15px; margin-top: 8px; }
  .contact { position: absolute; left: 40px; bottom: 60px; color: var(--white); }
  .contact__title { font-weight: 600; font-size: 17px; padding-bottom: 6px; margin-bottom: 12px;
    border-bottom: 2px solid var(--white); display: inline-block; }
  .contact__list { list-style: none; }
  .contact__item { display: flex; align-items: center; gap: 10px; font-size: 13px; margin-bottom: 7px; }
  .contact__item svg { width: 16px; height: 16px; flex: none; }
  .social { position: absolute; right: 16px; bottom: 32px; display: flex; align-items: center; gap: 7px;
    color: var(--white); font-size: 12px; }
  .social__dot { width: 16px; height: 16px; border-radius: 50%; background: var(--red); }

  /* front panel */
  .brand { position: absolute; left: 110px; top: 278px; }
  .brand__name { display: flex; align-items: center; gap: 10px; font-weight: 800; font-size: 28px;
    color: var(--ink); letter-spacing: .5px; line-height: 1; }
  .brand__mark { width: 16px; height: 16px; background: var(--blue); }
  .brand__trades { font-weight: 600; font-size: 14px; color: var(--ink); margin-top: 16px; }
  .pitch { position: absolute; left: 120px; top: 385px; }
  .pitch__lead { font-size: 14px; color: var(--ink); }
  .pitch__lead em { font-style: normal; color: var(--red); }
  .pitch__headline { font-family: "Teko", "Arial Narrow", sans-serif; font-weight: 500; font-size: 38px;
    line-height: .95; color: var(--charcoal); margin-top: 6px; }
  .pitch__headline span { color: var(--red); }
  .web { position: absolute; right: 24px; bottom: 18px; display: flex; align-items: center; gap: 8px;
    color: var(--white); font-size: 13px; }
  .web svg { width: 15px; height: 15px; }
</style>
</head>
<body>
<div class="canvas">
  <div class="folder">

    <section class="panel panel--back" aria-label="Back cover">
      <svg class="art" viewBox="0 0 509 720" aria-hidden="true">
        <polygon points="280,0 509,0 509,118" fill="var(--ink)"/>
        <line x1="280" y1="0" x2="509" y2="123" stroke="var(--blue)" stroke-width="6"/>
        <polyline points="0,400 420,570 509,480" fill="none" stroke="var(--red)" stroke-width="1"/>
        <polygon points="0,410 290,460 290,470 0,420" fill="var(--ink)"/>
        <polygon points="0,420 290,470 380,720 0,720" fill="var(--deep-red)"/>
        <polygon points="509,400 509,720 340,720" fill="var(--ink)"/>
      </svg>
      <div class="watermark">
        <div class="watermark__name">HARLOW<br>CONTRACTING</div>
        <div class="watermark__trades">Plumbing • Electrical • Hot Water</div>
      </div>
      <div class="contact">
        <div class="contact__title">Get in Touch</div>
        <ul class="contact__list">
          <li class="contact__item">
            <svg viewBox="0 0 16 16"><path d="M8 1a5 5 0 0 0-5 5c0 4 5 9 5 9s5-5 5-9a5 5 0 0 0-5-5z" fill="#fff"/><circle cx="8" cy="6" r="2" fill="var(--deep-red)"/></svg>
            Address Goes Here</li>
          <li class="contact__item">
            <svg viewBox="0 0 16 16"><circle cx="8" cy="8" r="8" fill="#fff"/><path d="M5 4l2 2-1 1c.5 1.2 1.8 2.5 3 3l1-1 2 2-1.5 1.5C7 12 4 9 3.5 5.5z" fill="var(--deep-red)"/></svg>
            0123 456 789</li>
          <li class="contact__item">
            <svg viewBox="0 0 16 16"><circle cx="8" cy="8" r="8" fill="#fff"/><rect x="4" y="5" width="8" height="6" fill="none" stroke="var(--deep-red)" stroke-width="1.2"/><path d="M4 5l4 3.5L12 5" fill="none" stroke="var(--deep-red)" stroke-width="1.2"/></svg>
            info@yourmailid.com</li>
          <li class="contact__item">
            <svg viewBox="0 0 16 16"><circle cx="8" cy="8" r="7" fill="none" stroke="#fff" stroke-width="1.4"/><ellipse cx="8" cy="8" rx="3" ry="7" fill="none" stroke="#fff" stroke-width="1.2"/><line x1="1" y1="8" x2="15" y2="8" stroke="#fff" stroke-width="1.2"/></svg>
            www.yourwebsite.com</li>
        </ul>
      </div>
      <div class="social">follow us : <span class="social__dot"></span><span class="social__dot"></span></div>
    </section>

    <section class="panel panel--front" aria-label="Front cover">
      <svg class="art" viewBox="0 0 509 720">
        <defs>
          <linearGradient id="tap-photo" x1="0" y1="0" x2="1" y2="1">
            <stop offset="0" stop-color="#c9b98a"/>
            <stop offset=".5" stop-color="#d8d6d0"/>
            <stop offset="1" stop-color="#eeeeec"/>
          </linearGradient>
        </defs>
        <polygon points="0,0 509,0 509,205 350,270 258,232 0,125" fill="url(#tap-photo)" role="img" aria-label="Photo of a chrome mixer tap over a bathroom basin"/>
        <line x1="0" y1="125" x2="258" y2="232" stroke="var(--blue)" stroke-width="6"/>
        <line x1="509" y1="192" x2="400" y2="236" stroke="var(--red)" stroke-width="3"/>
        <polygon points="0,600 170,700 150,720 0,720" fill="#ededed"/>
        <line x1="0" y1="570" x2="200" y2="690" stroke="var(--red)" stroke-width="1"/>
        <polygon points="509,430 509,520 260,720 150,720" fill="var(--ink)"/>
        <polygon points="260,720 509,520 509,720" fill="var(--deep-red)"/>
      </svg>
      <div class="brand">
        <div class="brand__name"><span class="brand__mark"></span>HARLOW<br>CONTRACTING</div>
        <div class="brand__trades">Plumbing • Electrical • Hot Water</div>
      </div>
      <div class="pitch">
        <p class="pitch__lead">Call 1 Number for <em>The Best in 3 Trades</em></p>
        <h1 class="pitch__headline">PLUMBING, <span>HOT WATER</span><br>&amp; ELECTRICAL</h1>
      </div>
      <div class="web">
        <svg viewBox="0 0 16 16"><circle cx="8" cy="8" r="7" fill="none" stroke="#fff" stroke-width="1.4"/><ellipse cx="8" cy="8" rx="3" ry="7" fill="none" stroke="#fff" stroke-width="1.2"/><line x1="1" y1="8" x2="15" y2="8" stroke="#fff" stroke-width="1.2"/></svg>
        www.yourwebsite.com
      </div>
    </section>

  </div>
</div>
</body>
</html>
```